VEX Quorum home page

I want a new look and design for the home page of www.vexquorum.example . Something new that better shows what our service is about. We provide live technical support to RE professionals via our smart phone app and website. The service is available for home inspectors, appraisers, real estate agents and others in the Real Estate Profession.

I just want a great looking home page design that demonstrates the service. Does not have to be a functional site, just the design.

Imagine walking around or through a house and having a technical question during your inspection. You pull out your phone, open the VEX Quo app and select a category, type in your question and it opens your camera to attach a photo. You submit your question and experts review it and send you an answer within minutes. Possibly while you are still on the job.

I am really looking for a way to convey that our service is all about RE professionals, like home inspectors, appraisers, RE agents getting help while they are in the field at the homes they are working at.   A home inspector looks at an electrical panel snaps a picture and sends their question to us and they get a response before they even leave the jobsite.  That feeling.

Reason: I would like to see the designs convey the feeling that our service is something every professional needs while doing their jobs. We have hundreds of inspectors using our service to get fast answers to very technical questions using our smart phone app.

Target Market(s)

Home Inspectors, Real Estate Appraisers, Real Estate Agents

Industry/Entity Type

Real Estate

Colors

Designer to choose colors to be used in the design.

Requirements
Must have
• People must understand we provide experts who respond to their real estate related technical support questions using our patent pending smart phone app.

```html
<!DOCTYPE html>
<html lang="en">
<head>
<meta charset="utf-8">
<title>VEX Quorum – Live Support Network</title>
<link href="https://fonts.googleapis.com/css2?family=Ubuntu:wght@300;400;500&family=Open+Sans:wght@400;600&display=swap" rel="stylesheet">
<style>
:root{
  --black:#000;
  --nav:#333333;
  --red:#e30b0c;
  --red-text:#e3100f;
  --white:#fff;
  --ink:#444;
  --body:#555;
  --footer:#e9e9e9;
}
*{margin:0;padding:0;box-sizing:border-box}
html,body{width:1200px;height:1143px;overflow:hidden;background:var(--white)}
body{position:relative;font-family:"Open Sans",sans-serif;color:var(--body)}
.site-header{position:absolute;left:0;top:0;width:1200px;height:113px;background:var(--black)}
.brand{position:absolute;left:124px;top:28px;display:flex;align-items:center;gap:10px;color:var(--white);font-family:"Ubuntu",sans-serif;font-weight:500;font-size:24px}
.brand-mark{width:40px;height:40px;border-radius:50%;background:var(--white)}
.account-links{position:absolute;right:118px;top:10px;font-family:"Ubuntu",sans-serif;font-size:14px;color:#aaa;letter-spacing:.3px}
.account-links span{margin:0 8px}
.store-badge{position:absolute;top:51px;height:41px;border:1px solid #444;border-radius:4px;background:#111;color:var(--white);font-family:"Open Sans",sans-serif;font-size:16px;display:flex;align-items:center;justify-content:center}
.store-droid{left:836px;width:124px}
.store-fruit{left:966px;width:122px}
.main-nav{position:absolute;left:0;top:113px;width:1200px;height:54px;background:var(--nav);border-bottom:2px solid #222}
.main-nav ul{list-style:none;display:flex;position:absolute;left:118px;top:0;height:54px}
.main-nav li{font-family:"Ubuntu",sans-serif;font-size:17.5px;color:var(--white);padding:0 18px;line-height:54px;border-right:1px solid #4a4a4a}
.main-nav li:last-child{border-right:0}
.hero{position:absolute;left:0;top:167px;width:1200px;height:447px;background:linear-gradient(#ec0f10,#d80909)}
.hero h1{position:absolute;left:122px;top:68px;font-family:"Ubuntu",sans-serif;font-weight:400;font-size:31px;line-height:39px;color:var(--white)}
.faq-list{position:absolute;left:122px;top:174px;width:456px;list-style:none;color:var(--white)}
.faq-list li{padding:0 0 8px;margin-bottom:10px;border-bottom:1px solid rgba(255,255,255,.35)}
.faq-list li:last-child{border-bottom:0}
.faq-q{font-family:"Open Sans",sans-serif;font-weight:600;font-size:15.5px;line-height:24px}
.faq-a{font-size:13.5px;line-height:20px;margin-top:1px}
.faq-a b{font-weight:600}
.dots{position:absolute;left:121px;top:370px;display:flex;gap:5px}
.dots i{width:12px;height:12px;border-radius:50%;background:rgba(255,255,255,.35)}
.dots i:first-child{background:var(--white)}
.app-phones{position:absolute;left:630px;top:45px;width:432px;height:362px}
.phone{position:absolute;border-radius:34px 34px 0 0}
.phone-back{left:232px;top:52px;width:200px;height:310px;background:#111;border:2px solid #333}
.phone-back .screen{position:absolute;left:8px;top:62px;right:14px;bottom:0;background:linear-gradient(#f2f2f2,#dcdcdc)}
.phone-front{left:0;top:0;width:250px;height:362px;background:linear-gradient(#fafafa,#d9d9d9);border:2px solid #bbb}
.phone-front .screen{position:absolute;left:12px;top:76px;right:12px;bottom:0;background:linear-gradient(#2a2a2a 0 44px,#e8e8e8 44px,#cfcfcf)}
.welcome{position:absolute;left:96px;top:574px;width:989px;height:459px;background:var(--white)}
.welcome h2{position:absolute;top:36px;width:100%;text-align:center;font-family:"Ubuntu",sans-serif;font-weight:300;font-size:33px;color:var(--ink)}
.welcome .intro{position:absolute;left:30px;top:90px;width:929px;text-align:center;font-size:12.6px;line-height:21.5px;color:var(--body)}
.steps{position:absolute;left:0;top:190px;width:100%;display:flex}
.step{position:absolute;width:220px;text-align:center}
.step-icon{width:136px;height:136px;margin:0 auto;border-radius:50%;background:var(--white);box-shadow:0 0 6px rgba(0,0,0,.25);display:flex;align-items:center;justify-content:center}
.step-icon span{width:124px;height:124px;border-radius:50%;background:var(--black);display:flex;align-items:center;justify-content:center}
.step h3{margin-top:14px;font-family:"Open Sans",sans-serif;font-weight:400;font-size:17.5px;color:var(--red-text)}
.step p{margin-top:6px;font-size:13px;line-height:20px;color:var(--body)}
.site-footer{position:absolute;left:96px;top:1033px;width:989px;height:110px;background:var(--footer)}
.footer-nav{position:absolute;left:44px;top:30px;font-family:"Ubuntu",sans-serif;font-size:14.5px;color:var(--ink)}
.footer-nav span{margin:0 9px}
.copyright{position:absolute;left:46px;top:64px;font-size:12px;color:var(--body)}
.social{position:absolute;left:845px;top:28px;display:flex;gap:4px}
.social i{width:26px;height:26px;border-radius:50%;background:#111}
</style>
</head>
<body>
<header class="site-header">
  <div class="brand"><span class="brand-mark"></span>VEX Quo</div>
  <div class="account-links">JOIN US<span>|</span>LOGIN</div>
  <div class="store-badge store-droid">Droid Shelf</div>
  <div class="store-badge store-fruit">Fruit Depot</div>
</header>

<nav class="main-nav">
  <ul>
    <li>HOME</li><li>MEMBERSHIP</li><li>DETAILS</li><li>FAQ</li><li>ABOUT US</li><li>FEATURES</li><li>PLAN COMPARISON</li>
  </ul>
</nav>

<section class="hero">
  <h1>Join the VEX Quorum<br>Live Support Network Today!</h1>
  <ul class="faq-list">
    <li><p class="faq-q">Q: Lorem ipsum dolor sit amet consectetuer adipiscing elit ?</p><p class="faq-a"><b>A:</b> Nulla sit amet diam Duis non nunc libero a tempus libero lectus</p></li>
    <li><p class="faq-q">Q: Pellentesque faucibus Ut accumsan?</p><p class="faq-a"><b>A:</b> Nulla sit amet diam Duis non nunc libero a tempus libero lectus feugiat felis Morbi diam mauris viverra in gravida</p></li>
    <li><p class="faq-q">Q: Lorem ipsum dolor sit amet consectetuer adipiscing elit ?</p><p class="faq-a"><b>A:</b> Nulla sit amet diam Duis non nunc libero a tempus libero lectus</p></li>
  </ul>
  <div class="dots"><i></i><i></i><i></i><i></i></div>
  <div class="app-phones" role="img" aria-label="Two smartphones showing the app's Ask Question and Submit Question screens">
    <div class="phone phone-back"><div class="screen"></div></div>
    <div class="phone phone-front"><div class="screen"></div></div>
  </div>
</section>

<main class="welcome">
  <h2>Welcome to Our Website Homepage</h2>
  <p class="intro">Aliquam nec erat at purus cursus interdum Vestibulum ligula augue bibendum accumsan vestibulum ut commodo a mi Morbi ornare gravida elit Integer congue augue et malesuada iaculis ipsum dui aliquet felis at cursus magna nisl nec elit Vestibulum gravida Praesent elementum elit at tellus Malesuada nec ultricies sit amet porttitor mattis enim In massa libero interdum nec interdum vel blandit sed nulla In ullamcorper est eget tempor cursus neque mi consectetue</p>
  <div class="steps">
    <div class="step" style="left:39px">
      <div class="step-icon"><span>
        <svg width="62" height="62" viewBox="0 0 62 62" fill="none" stroke="#fff" stroke-width="4"><path d="M4 10l5 5 9-10"/><rect x="4" y="26" width="11" height="11"/><rect x="4" y="46" width="11" height="11"/><path d="M24 12h34M24 32h34M24 52h34"/></svg>
      </span></div>
      <h3>Select the Category</h3>
      <p>Vestibulum gravida Praesent<br>elementum elit at tellus</p>
    </div>
    <div class="step" style="left:279px">
      <div class="step-icon"><span>
        <svg width="68" height="64" viewBox="0 0 68 64"><path d="M34 2C16 2 2 14 2 29c0 9 5 16 12 21l-4 12 15-8c3 1 6 1 9 1 18 0 32-12 32-27S52 2 34 2z" fill="#fff"/><text x="34" y="44" text-anchor="middle" font-family="Ubuntu,sans-serif" font-weight="500" font-size="38" fill="#000">?</text></svg>
      </span></div>
      <h3>Enter your Question</h3>
      <p>Vestibulum gravida Praesent<br>elementum elit at tellus</p>
    </div>
    <div class="step" style="left:520px">
      <div class="step-icon"><span>
        <svg width="66" height="52" viewBox="0 0 66 52"><path d="M6 10h14l5-8h16l5 8h14a4 4 0 0 1 4 4v32a4 4 0 0 1-4 4H6a4 4 0 0 1-4-4V14a4 4 0 0 1 4-4z" fill="#fff"/><circle cx="33" cy="29" r="13" fill="#000"/><circle cx="33" cy="29" r="7" fill="#fff"/></svg>
      </span></div>
      <h3>Add Photos if you like</h3>
      <p>Vestibulum gravida Praesent<br>elementum elit at tellus</p>
    </div>
    <div class="step" style="left:760px">
      <div class="step-icon"><span>
        <svg width="66" height="66" viewBox="0 0 66 66"><circle cx="33" cy="33" r="31" fill="#fff"/><path d="M18 34l10 10 20-22" fill="none" stroke="#000" stroke-width="8" stroke-linecap="round" stroke-linejoin="round"/></svg>
      </span></div>
      <h3>Submit your Question</h3>
      <p>Vestibulum gravida Praesent<br>elementum elit at tellus</p>
    </div>
  </div>
</main>

<footer class="site-footer">
  <div class="footer-nav">HOME<span>|</span>MEMBERSHIP<span>|</span>DETAILS<span>|</span>FAQ<span>|</span>ABOUT US<span>|</span>FEATURES<span>|</span>PLAN COMPARISON</div>
  <p class="copyright">© 2013 Company Name.&nbsp; All right reserved.&nbsp; Term of Use</p>
  <div class="social" aria-label="Social links"><i></i><i></i><i></i><i></i></div>
</footer>
</body>
</html>
```